Sudden Tides "Lantern Road" New Single Cover

Create cover artwork for the band Sudden Tides' new single "Lantern Road" being released early 2020. Style, font and graphics to be consistent with band's previous releases and overall brand identity. Visit www.suddentidesband.example and our Spotify page https://music.example.net/artist/7QzWpLx3RtVnKd8e2YbHcJ?si=MUrTgKa4PLe7skvWq2AmZd to view our previous releases and overall brand identity. Some examples attached as well. We are looking for someone to work with on future projects as well.

Lyrics are here: https://docs.example.org/document/d/3KTp9wrn_2ZQa8eXb4Lo_fimH7C5m83Jz4Pd70hrtVcA/edit

Music is here: https://audiostream.example.com/suddentides/lantern-road/s-pzkwa

Font styles to use
Sans Serif

Colors

Designer to choose colors to be used in the design.

Requirements
Must have
• Must be consistent with current brand identity and with prior album / single art.

```html
<!DOCTYPE html>
<html lang="en">
<head>
<meta charset="utf-8">
<title>Sudden Tides – Lantern Road</title>
<link href="https://fonts.googleapis.com/css2?family=Questrial&display=swap" rel="stylesheet">
<style>
  :root {
    --tide-teal: #17a6ac;
    --lantern-orange: #fbb01a;
    --burst-mint: #5be3a8;
    --panel-teal: #2ba7ad;
    --band-white: #ffffff;
  }
  html, body {
    margin: 0;
    padding: 0;
    width: 1200px;
    height: 1200px;
    overflow: hidden;
    background: var(--tide-teal);
  }
  .cover {
    display: block;
    width: 1200px;
    height: 1200px;
  }
  .cover-background { fill: var(--tide-teal); }
  .title-letter {
    font-family: "Questrial", sans-serif;
    font-size: 440px;
    fill: none;
    stroke: var(--lantern-orange);
    stroke-width: 7;
    stroke-linejoin: round;
  }
  .ornament-area { fill: url(#ornament-glow); }
  .band-name {
    font-family: "Questrial", sans-serif;
    font-size: 80px;
    fill: var(--band-white);
  }
</style>
</head>
<body>
<svg class="cover" viewBox="0 0 1200 1200" xmlns="http://www.w3.org/2000/svg">
  <defs>
    <radialGradient id="ornament-glow" cx="50%" cy="50%" r="55%">
      <stop offset="0%" stop-color="#2ba7ad"/>
      <stop offset="45%" stop-color="#48c9a9"/>
      <stop offset="100%" stop-color="#2ba7ad"/>
    </radialGradient>
  </defs>

  <rect class="cover-background" width="1200" height="1200"/>

  <g class="single-title" aria-label="Lantern Road">
    <g class="title-line-one">
      <text class="title-letter" x="40" y="503" textLength="135" lengthAdjust="spacingAndGlyphs">L</text>
      <text class="title-letter" x="204" y="503" textLength="135" lengthAdjust="spacingAndGlyphs">A</text>
      <text class="title-letter" x="368" y="503" textLength="135" lengthAdjust="spacingAndGlyphs">N</text>
      <text class="title-letter" x="532" y="503" textLength="135" lengthAdjust="spacingAndGlyphs">T</text>
      <text class="title-letter" x="696" y="503" textLength="135" lengthAdjust="spacingAndGlyphs">E</text>
      <text class="title-letter" x="860" y="503" textLength="135" lengthAdjust="spacingAndGlyphs">R</text>
      <text class="title-letter" x="1024" y="503" textLength="135" lengthAdjust="spacingAndGlyphs">N</text>
    </g>

    <g class="title-line-two">
      <text class="title-letter" x="100" y="870" textLength="220" lengthAdjust="spacingAndGlyphs">R</text>
      <rect class="ornament-area" x="345" y="520" width="360" height="368" role="img" aria-label="Radiating mint sunburst ornament standing in for the letter O"/>
      <text class="title-letter" x="735" y="870" textLength="190" lengthAdjust="spacingAndGlyphs">A</text>
      <text class="title-letter" x="950" y="870" textLength="165" lengthAdjust="spacingAndGlyphs">D</text>
    </g>
  </g>

  <text class="band-name" x="291" y="1041" textLength="580" lengthAdjust="spacing">SUDDEN TIDES</text>
</svg>
</body>
</html>
```